" * Trabalhamos com limpeza de pele com hidro sucção e tratamentos de rejuvenescimento. * Clareamento de pele, depilação com luz pulsada e radiofrequência. * Tratamentos corporais como: massagem relaxante, modeladora, drenagem linfatica, corrente russa, endermoterapia, lipocavitação "

```html
<!DOCTYPE html>
<html lang="pt-BR">
<head>
<meta charset="utf-8">
<title>Studio Lumina — Estética Facial e Corporal</title>
<link rel="stylesheet" href="https://fonts.googleapis.com/css2?family=Kaushan+Script&family=Open+Sans:wght@400;600;700&display=swap">
<style>
  :root {
    --teal: #1f8a98;
    --teal-dark: #146b77;
    --teal-soft: #cfe6ea;
    --mist: #eaf2f4;
    --lime: #b8cd6a;
    --ink: #3d4c52;
    --muted: #7b8b91;
    --white: #ffffff;
    --stage: #e4e7ea;
  }
  * { box-sizing: border-box; margin: 0; padding: 0; }
  html, body { width: 1200px; height: 1200px; overflow: hidden; }
  body {
    background: var(--stage);
    font-family: "Open Sans", sans-serif;
    color: var(--ink);
    position: relative;
  }
  .page {
    position: absolute; left: 250px; top: 20px;
    width: 700px; height: 1160px;
    background: var(--mist);
    display: flex; flex-direction: column;
    box-shadow: 0 4px 18px rgba(0,0,0,.12);
  }
  /* header */
  .site-header {
    height: 44px; background: var(--white);
    display: flex; align-items: center; justify-content: space-between;
    padding: 0 28px; border-top: 4px solid var(--teal);
  }
  .brand { display: flex; align-items: center; gap: 8px; font-size: 15px; font-weight: 600; color: var(--teal); }
  .brand-dot { width: 12px; height: 12px; border-radius: 50%; background: var(--teal); }
  .nav { display: flex; gap: 22px; font-size: 11px; color: var(--muted); text-transform: uppercase; letter-spacing: .5px; }
  /* hero */
  .hero {
    height: 250px; position: relative;
    background: linear-gradient(180deg, #f6fafb 0%, #e3eff2 100%);
  }
  .hero-photo {
    position: absolute; left: 70px; top: 0; width: 300px; height: 250px;
    background: radial-gradient(ellipse at 50% 45%, #f3dccb 0%, #e8cdb9 40%, #d8e9ee 75%, #e3eff2 100%);
  }
  .hero-title {
    position: absolute; right: 70px; top: 78px;
    font-family: "Kaushan Script", cursive; font-size: 54px; color: var(--teal);
  }
  .hero-tabs { position: absolute; left: 210px; bottom: 18px; display: flex; gap: 14px; }
  .hero-tab {
    width: 90px; height: 30px; background: var(--lime); color: var(--white);
    font-size: 11px; font-weight: 600; display: flex; align-items: center; justify-content: center;
  }
  /* about band */
  .about {
    height: 130px; background: var(--teal-dark); color: var(--white);
    text-align: center; padding: 16px 120px 0;
  }
  .about h2 { font-size: 14px; font-weight: 600; margin-bottom: 8px; }
  .about p { font-size: 10px; line-height: 1.55; opacity: .9; }
  .about .btn {
    display: inline-block; margin-top: 8px; background: var(--white); color: var(--teal-dark);
    font-size: 8px; font-weight: 700; padding: 3px 10px; text-transform: uppercase;
  }
  /* care circles */
  .care { height: 230px; padding-top: 26px; text-align: center; background: var(--white); }
  .circles { display: flex; justify-content: center; align-items: center; }
  .circle {
    width: 118px; height: 118px; border-radius: 50%;
    border: 3px solid var(--teal-soft); background: var(--white);
    display: flex; align-items: center; justify-content: center;
    font-size: 10px; color: var(--teal); padding: 18px; line-height: 1.4;
  }
  .circle.main {
    width: 140px; height: 140px; margin: 0 -10px; z-index: 1;
    background: var(--teal); border-color: var(--white); color: var(--white);
    flex-direction: column; gap: 6px; font-weight: 600; font-size: 10px;
    box-shadow: 0 0 0 3px var(--teal-soft);
  }
  .care p { font-size: 10px; color: var(--muted); margin: 16px auto 0; width: 340px; line-height: 1.5; }
  /* services */
  .services { height: 300px; background: var(--mist); padding-top: 20px; text-align: center; }
  .services h2 { font-size: 15px; color: var(--teal); font-weight: 600; }
  .services .lead { font-size: 10px; color: var(--muted); margin-top: 4px; }
  .cards { display: flex; justify-content: center; gap: 16px; margin-top: 18px; }
  .card { width: 150px; background: var(--white); }
  .card-photo { height: 150px; }
  .card-photo.facial { background: linear-gradient(160deg, #f1ddcf, #d9c3b6 60%, #cfe2e6); }
  .card-photo.drain { background: linear-gradient(160deg, #eac9b4, #f4e4d9 55%, #c9dde2); }
  .card-photo.massage { background: linear-gradient(160deg, #f5e6dc, #e2c2ab 55%, #d6e8ec); }
  .card-caption { height: 28px; background: var(--lime); color: var(--white); font-size: 10px; font-weight: 600; display: flex; align-items: center; justify-content: center; }
  /* footer */
  .site-footer {
    flex: 1; background: linear-gradient(180deg, #9fbfc6, #7fa6ae);
    display: flex; align-items: center; justify-content: space-between; padding: 0 50px; color: var(--white);
  }
  .footer-brand .brand { color: var(--white); font-size: 20px; }
  .footer-brand .brand-dot { background: var(--white); }
  .footer-brand .tag { font-size: 11px; font-weight: 600; text-transform: uppercase; margin: 6px 0 8px; letter-spacing: .5px; }
  .footer-brand .contact { font-size: 10px; line-height: 1.6; }
  .footer-side { text-align: right; }
  .footer-side h3 { font-size: 11px; font-weight: 600; text-transform: uppercase; }
  .footer-side .hours { font-size: 10px; margin: 4px 0 10px; }
  .thumbs { display: flex; gap: 6px; justify-content: flex-end; }
  .thumb { width: 44px; height: 34px; background: linear-gradient(150deg, #e9d2c3, #c9dfe3); }
</style>
</head>
<body>
<main class="page">
  <header class="site-header">
    <div class="brand"><span class="brand-dot"></span>Studio Lumina</div>
    <nav class="nav"><span>Início</span><span>Sobre</span><span>Serviços</span><span>Contato</span></nav>
  </header>

  <section class="hero">
    <div class="hero-photo" role="img" aria-label="Foto de cliente sorrindo com toalha no cabelo durante tratamento facial"></div>
    <h1 class="hero-title">Fique Linda</h1>
    <div class="hero-tabs"><span class="hero-tab">Facial</span><span class="hero-tab">Corporal</span></div>
  </section>

  <section class="about">
    <h2>Sobre o Studio</h2>
    <p>Trabalhamos com limpeza de pele com hidro sucção e tratamentos de rejuvenescimento, clareamento de pele, depilação com luz pulsada e radiofrequência. Cuidamos de você com carinho e técnicas modernas para realçar sua beleza natural.</p>
    <span class="btn">Saiba mais</span>
  </section>

  <section class="care">
    <div class="circles">
      <div class="circle">Limpeza de pele e rejuvenescimento</div>
      <div class="circle main">
        <svg width="26" height="26" viewBox="0 0 24 24" aria-hidden="true"><path d="M12 2 C12 2 5 10 5 15 a7 7 0 0 0 14 0 C19 10 12 2 12 2z" fill="#ffffff"/></svg>
        <span>Cuidados da pele e do corpo</span>
      </div>
      <div class="circle">Luz pulsada e radiofrequência</div>
    </div>
    <p>O Studio Lumina é o seu espaço para relaxar e cuidar da saúde e da beleza com bem-estar.</p>
  </section>

  <section class="services">
    <h2>Estética Corporal e Facial</h2>
    <p class="lead">Massagem, drenagem linfática, endermoterapia e lipocavitação para o seu corpo.</p>
    <div class="cards">
      <article class="card"><div class="card-photo facial" role="img" aria-label="Foto de tratamento de rejuvenescimento facial"></div><div class="card-caption">Rejuvenescimento</div></article>
      <article class="card"><div class="card-photo drain" role="img" aria-label="Foto de drenagem linfática no rosto"></div><div class="card-caption">Drenagem</div></article>
      <article class="card"><div class="card-photo massage" role="img" aria-label="Foto de massagem relaxante"></div><div class="card-caption">Massagem</div></article>
    </div>
  </section>

  <footer class="site-footer">
    <div class="footer-brand">
      <div class="brand"><span class="brand-dot"></span>Studio Lumina</div>
      <div class="tag">Estética facial e corporal</div>
      <div class="contact">Rua das Acácias, 120 · Centro<br>(11) 4002-3100<br>contato@studiolumina.com</div>
    </div>
    <div class="footer-side">
      <h3>Agende seu horário</h3>
      <div class="hours">Seg a Sáb · 9h às 19h</div>
      <div class="thumbs">
        <div class="thumb" role="img" aria-label="Foto do ambiente do espaço"></div>
        <div class="thumb" role="img" aria-label="Foto de tratamento corporal"></div>
        <div class="thumb" role="img" aria-label="Foto de produtos de estética"></div>
      </div>
    </div>
  </footer>
</main>
</body>
</html>
```